Flyer-Design für Flugzeugvercharterung
Zielgruppe
Talwerk Luftdienst ist ein junges Unternehmen in dem Bereich Flugzeugvercharterung für Falbrecht Flugbau Flugzeuge.
Wir haben es uns zum Ziel gemacht, unseren Kunden Flugstunden zu einem fairen Preis anzubieten.
Sicherheit beim Fliegen steht für uns im Fokus – jederzeit sorgen wir für einen einwandfreien Zustand der Technik. Die Wartung und Instandhaltung unserer Flotte wird dabei durch die Herstellerwerft Falbrecht Flugbau gewährleistet. Fliegen Sie mit uns und lernen Sie die Vorteile unseres Charter-Unternehmens kennen!
Aufgabenstellung
Der Flyer muss ansprechend sein.
Der Flyer muss modern sein - aber nicht verspielt.
Der Kunde muss den Flyer in die Hand nehmen und einen "Wow" Effekt erhalten.
Nutzen Sie alle informationen auf unserer Webpage: www.TL-Luftdienst.de
Es sollen mindestens dreifach sein - evtl sogar vierfach! (Also drei pro Seite, wenn der flyer gewendet wird)
Wir bieten eines der modernsten Flugzeuge im General Aviation Bereich an. Dies soll der Kunde sofort erkennen. Gleichzeitig sind wir sehr professionell - aber keine Spießer-Firma.
Profi ja - Spießer nein.
Mein Kooperationspartern hat in meinen Augen einen sehr guten Flyer erstellt (siehe Anhang).
Ebenfalls habe ich "meinen" Versuch eines Flyers mal angehängt.
Was benötigen wir?
- Einen modernen aber stylischen Auftritt
- Alles auf einen Blick
- Gute Ausführungen unserer Flugzeuge (hierzu kann gerne die HP genutzt werden "www.TL-Luftdienst.de"
- Anlehnung an die Homepage www.TL-Luftdienst.de
So kann evtl ein direkter Bezug hergestellt werden.

```html
<!DOCTYPE html>
<html lang="de">
<head>
<meta charset="utf-8">
<title>Talwerk Luftdienst – Flyer</title>
<link href="https://fonts.googleapis.com/css2?family=Exo+2:wght@300;400&family=Open+Sans:wght@400;600;700&display=swap" rel="stylesheet">
<style>
:root{
  --navy:#2d323f;
  --blue:#1a9ad6;
  --blue-deep:#1f4f94;
  --white:#ffffff;
  --ink:#3a3f48;
  --stage:#ffffff;
  --backdrop:#c9ccce;
  --grey-light:#d3d8dc;
  --grey-dark:#98a2ab;
}
*{margin:0;padding:0;box-sizing:border-box}
html,body{width:1200px;height:3224px;overflow:hidden;background:var(--stage)}
body{position:relative;font-family:"Open Sans",Arial,sans-serif}
.sheet{position:absolute;width:980px;height:693px;overflow:hidden}
.sheet svg.art{position:absolute;left:0;top:0;width:980px;height:693px}
.outside{background:var(--navy)}
.inside{background:radial-gradient(ellipse at 50% 45%,var(--grey-light) 0%,#bfc6cc 55%,var(--grey-dark) 100%)}
.panel{position:absolute;top:0;height:693px;width:327px}
.p1{left:0}.p2{left:327px;width:326px}.p3{left:653px}
.heading{position:absolute;font-family:"Exo 2",Arial,sans-serif;font-weight:300;color:var(--blue);font-size:21px;letter-spacing:.3px;text-transform:uppercase;line-height:1.1;white-space:nowrap}
.heading.on-blue{color:var(--white)}
.body{position:absolute;font-size:11px;line-height:16.3px;text-align:justify;hyphens:auto}
.body p{margin-bottom:16px}
.outside .body{color:#e9ebef}
.inside .body{color:var(--ink)}
.claim{position:absolute;font-family:"Exo 2",Arial,sans-serif;font-weight:300;color:var(--white);text-transform:uppercase;font-size:22px;line-height:24px}
.wordmark{position:absolute;font-weight:700;color:var(--blue-deep);font-size:15px;letter-spacing:.2px;white-space:nowrap}
.photo-right{position:absolute;left:0;top:0;width:327px;height:655px;background:linear-gradient(180deg,#cfd6da 0%,#e6dcc0 30%,#b9a88a 60%,#6c6e70 100%)}
.contact{position:absolute;right:26px;text-align:right;color:var(--white);font-size:12.5px;line-height:16.5px;white-space:nowrap}
.subline{position:absolute;right:26px;font-family:"Exo 2",Arial,sans-serif;color:var(--blue);font-size:10px;font-variant:small-caps;letter-spacing:.3px;white-space:nowrap}
.intro{position:absolute;color:var(--white);font-size:13.5px;line-height:16px}
.courses{position:absolute;color:var(--white);font-size:10.6px;line-height:15px;list-style:none;white-space:nowrap}
.prices{color:var(--blue)}
.chart-col{position:absolute;top:54px;width:146px;font-size:10.3px;line-height:16.3px;color:#eef0f3;text-align:justify;hyphens:auto}
.chart-col p{margin-bottom:16px}
.mock{position:absolute;left:173px;width:838px;height:671px;background:var(--backdrop);overflow:hidden}
.mock .sheet{left:27px;top:58px;transform:scale(.8);transform-origin:0 0}
</style>
</head>
<body>

<!-- ========== OUTSIDE SPREAD ========== -->
<section class="sheet outside" style="left:118px;top:125px">
  <svg class="art" viewBox="0 0 980 693">
    <path d="M327,471 C380,600 500,662 653,656 L653,693 L327,693 Z" fill="#fbfbfb"/>
    <rect x="653" y="655" width="327" height="38" fill="#fbfbfb"/>
    <path d="M352,515 C362,420 440,348 560,336" fill="none" stroke="var(--blue)" stroke-width="9" stroke-linecap="round"/>
    <circle cx="164" cy="71" r="98" fill="var(--blue)"/>
    <path d="M66,120 C40,40 130,-20 230,0 C320,20 300,140 200,170" fill="none" stroke="#e6e8ec" stroke-width="1.6"/>
    <g role="img" aria-label="Foto: Kleinflugzeug auf dem Vorfeld"><circle cx="118" cy="600" r="92" fill="#b8c2b6"/></g>
    <circle cx="128" cy="598" r="104" fill="none" stroke="#e6e8ec" stroke-width="1.4"/>
  </svg>

  <div class="panel p1">
    <div class="claim" style="right:70px;top:42px;text-align:right">Your<br>Aviation<br>Partner</div>
    <h2 class="heading" style="left:32px;top:213px">Über uns</h2>
    <div class="body" style="left:32px;top:248px;width:258px">
      <p>Talwerk Luftdienst ist ein Charter-Unternehmen, das es sich zur Aufgabe gemacht hat, Hobby- bzw. Berufspiloten faire, preiswerte Flugstunden zu ermöglichen! Auch Flugbegeisterte können bei unseren Schnupperflügen die Welt von oben betrachten und auf Wunsch ihre Pilotenausbildung bei uns beginnen.</p>
      <p>Sehr gerne informieren wir Sie zu unserem Leistungsangebot – rufen Sie an oder kommen Sie bei uns in Wendelsau vorbei.</p>
    </div>
  </div>

  <div class="panel p2">
    <h2 class="heading" style="right:26px;top:30px">So finden Sie uns</h2>
    <div class="body" style="left:30px;top:70px;width:270px;font-size:10.2px;line-height:16px">
      <p>Wir sind in Wendelsau im Haus von Falbrecht Flugbau untergebracht. Mit dem Auto können Sie auf das Gelände von Falbrecht Flugbau fahren und es auf den Parkplätzen neben dem Gebäude parken. Auf dieser Seite befindet sich ebenfalls der Eingang. Wir sind täglich ab 09:30 Uhr für Sie da.</p>
      <p>Im Foyer liegen unsere Flyer und Informationsbroschüren aus – hier finden Sie alle notwendigen Informationen vor.</p>
      <p>Besuchen Sie uns mit den öffentlichen Verkehrsmitteln: Fahren Sie mit der S-Bahn S3 bis zum Bahnhof Wendelsau und folgen anschließend dem Fußweg in Richtung des Flugplatzes Wendelsau in südlicher Richtung.</p>
    </div>
    <h2 class="heading" style="right:26px;top:377px">Kontakt</h2>
    <div class="subline" style="top:404px">Im Haus von Falbrecht Flugbau</div>
    <div class="contact" style="top:443px">Lindenhof-Weg 12<br>63411 Wendelsau<br>Tel.: 06104 - 555 120 40<br>e-mail: info@tl-luftdienst.de<br>www.tl-luftdienst.de</div>
    <div class="wordmark" style="left:20px;top:640px">Talwerk Luftdienst</div>
  </div>

  <div class="panel p3">
    <div class="photo-right" role="img" aria-label="Foto: Skyline einer Großstadt mit Kleinflugzeug im Flug"></div>
    <svg style="position:absolute;left:0;top:0" width="327" height="693" viewBox="0 0 327 693">
      <circle cx="197" cy="96" r="147" fill="var(--blue)" opacity=".92"/>
      <path d="M60,520 C10,420 80,330 200,330 C300,330 330,420 300,470" fill="none" stroke="#ffffff" stroke-width="3" opacity=".85"/>
    </svg>
    <div class="claim" style="left:85px;top:58px">Noch nie war<br>fliegen so<br>sicher &amp; günstig<br>zugleich</div>
    <div class="wordmark" style="right:20px;top:664px">Talwerk Luftdienst</div>
  </div>
</section>

<!-- ========== INSIDE SPREAD ========== -->
<section class="sheet inside" style="left:118px;top:875px">
  <svg class="art" viewBox="0 0 980 693">
    <circle cx="103" cy="78" r="120" fill="var(--blue)"/>
    <path d="M20,110 C10,60 40,20 100,10" fill="none" stroke="#ffffff" stroke-width="2.5"/>
    <g role="img" aria-label="Foto: Stadt-Skyline im Abendlicht"><circle cx="115" cy="585" r="84" fill="#c29c78"/></g>
    <circle cx="118" cy="580" r="96" fill="none" stroke="#ffffff" stroke-width="1.4"/>
    <circle cx="490" cy="112" r="130" fill="var(--blue)"/>
    <circle cx="492" cy="106" r="140" fill="none" stroke="#ffffff" stroke-width="1.4"/>
    <g role="img" aria-label="Foto: Kleinflugzeug auf der Startbahn"><circle cx="490" cy="700" r="118" fill="#a8b1a5"/></g>
    <path d="M420,690 C430,620 520,600 600,640" fill="none" stroke="#ffffff" stroke-width="1.4"/>
    <path d="M620,0 C570,150 600,330 720,385 C800,415 900,400 980,385 L980,0 Z" fill="var(--navy)"/>
    <g role="img" aria-label="Foto: Cockpit-Instrumente"><circle cx="874" cy="533" r="108" fill="#44474b"/></g>
    <path d="M775,560 C760,480 820,420 900,425 C980,430 990,520 960,560" fill="none" stroke="#ffffff" stroke-width="2"/>
    <path d="M780,610 C840,650 940,640 980,600" fill="none" stroke="#ffffff" stroke-width="1.4"/>
  </svg>

  <div class="panel p1">
    <h2 class="heading on-blue" style="left:49px;top:58px;font-size:20px">Rundflüge</h2>
    <div class="intro" style="left:49px;top:84px;width:130px">Die Welt von oben sehen –<br>Wir machen es möglich</div>
    <div class="body" style="left:43px;top:208px;width:268px;font-size:10.3px;line-height:16px">
      <p>Die Frankfurter Skyline aus der Vogelperspektive betrachten? Das eigene Haus, Ihre Wohnung oder den Garten von oben sehen? Dann sind Sie bei der Talwerk Luftdienst in Wendelsau genau richtig.</p>
      <p style="margin-bottom:0">So könnte Ihr Rundflug aussehen:</p>
      <p><b>Beispiel 1:</b> Platzrunden-Rundflug mit 1 Person (max. 100 Kg) ab Wendelsau für 29€</p>
      <p><b>Beispiel 2:</b> 30 Minuten Rundflug für 1 Person (max. 100 Kg) ab Wendelsau für 109€ (ideal für einen Skyline Rundflug), aktuell für 99€.</p>
      <p><b>Beispiel 3:</b> 30 Minuten Rundflug mit bis zu 3 Personen (insg. max. 200 Kg) ab Wendelsau für 199€ regulär (ideal für einen Skyline Rundflug), aktuell für 179€.</p>
    </div>
  </div>

  <div class="panel p2">
    <h2 class="heading on-blue" style="left:0;width:326px;text-align:center;top:82px;font-size:19px">Pilotenausbildung</h2>
    <ul class="courses" style="left:60px;top:118px"><li>• PPL-A</li><li>• IFR</li><li>• ATPL-A</li><li>• AZF</li><li>• En-Route IFR</li></ul>
    <ul class="courses" style="left:150px;top:118px"><li>• MEP (auf der • FB42)</li><li>• CPL</li><li>• BZF I+II</li><li>• Nachtflugausbildung</li><li>• Competency IR</li></ul>
    <div class="body" style="left:43px;top:282px;width:240px;font-size:10.3px;line-height:16px">
      <p>In Zusammenarbeit mit unseren Kooperationspartnern können Sie bei der Talwerk Luftdienst ab sofort Pilot werden! Sie haben die Möglichkeit im Rahmen unserer Pilotenausbildung die Flugscheine PPL-A bis ATPL-A zu erreichen.</p>
      <p>Ihre praktische Flugausbildung werden Sie auf der modernen Flotte von Talwerk Luftdienst durchführen. Der Vorteil dabei: Sie werden von den klassischen Fluginstrumenten bis hin zum modernen „Glascockpit“ ein abgerundetes Angebot erhalten – und jederzeit selbst entscheiden dürfen, ob Sie klassische Instrumente oder moderne Anzeigegeräte bevorzugen.</p>
    </div>
  </div>

  <div class="panel p3">
    <h2 class="heading" style="left:7px;top:12px;font-size:24px">Charter &amp; Flotte</h2>
    <div class="chart-col" style="left:7px">
      <p>Unsere Preise verstehen sich inklusive 19 % Mehrwertsteuer und Treibstoffkosten. Landegebühren, Abstellgebühren sowie Handling-Fees der jeweiligen Airports usw. sind nicht im Preis enthalten.</p>
      <p>Abgerechnet wird nach Blockstunden in den jeweiligen Flugzeugen. Die Stundenzähler werden vor und nach jedem Flug von einem unserer Mitarbeiter gemeinsam mit Ihnen abgelesen</p>
    </div>
    <div class="chart-col" style="left:166px;width:145px">
      <p>und in das Übergabeprotokoll eingetragen. So haben Sie eine transparente Übersicht. Zu jeder Abrechnung erhalten Sie vor Ort eine Rechnung.</p>
      <p class="prices">• FB20-100 mit Navis 660 159€ pro Stunde Nassmiete</p>
      <p class="prices">• FB40 IFR/AP OE-KTA 249€ pro Stunde Nassmiete</p>
      <p class="prices">• FB42 TDI OE-KTC 519€ pro Stunde Nassmiete</p>
    </div>
  </div>
</section>

<!-- ========== PRESENTATION: OUTSIDE ========== -->
<div class="mock" style="top:1631px">
  <section class="sheet outside">
    <svg class="art" viewBox="0 0 980 693">
      <path d="M327,471 C380,600 500,662 653,656 L653,693 L327,693 Z" fill="#fbfbfb"/>
      <rect x="653" y="655" width="327" height="38" fill="#fbfbfb"/>
      <path d="M352,515 C362,420 440,348 560,336" fill="none" stroke="var(--blue)" stroke-width="9" stroke-linecap="round"/>
      <circle cx="164" cy="71" r="98" fill="var(--blue)"/>
      <path d="M66,120 C40,40 130,-20 230,0 C320,20 300,140 200,170" fill="none" stroke="#e6e8ec" stroke-width="1.6"/>
      <g role="img" aria-label="Foto: Kleinflugzeug auf dem Vorfeld"><circle cx="118" cy="600" r="92" fill="#b8c2b6"/></g>
    </svg>
    <div class="panel p1">
      <div class="claim" style="right:70px;top:42px;text-align:right">Your<br>Aviation<br>Partner</div>
      <h2 class="heading" style="left:32px;top:213px">Über uns</h2>
      <div class="body" style="left:32px;top:248px;width:258px">
        <p>Talwerk Luftdienst ist ein Charter-Unternehmen, das es sich zur Aufgabe gemacht hat, Hobby- bzw. Berufspiloten faire, preiswerte Flugstunden zu ermöglichen! Auch Flugbegeisterte können bei unseren Schnupperflügen die Welt von oben betrachten und auf Wunsch ihre Pilotenausbildung bei uns beginnen.</p>
        <p>Sehr gerne informieren wir Sie zu unserem Leistungsangebot – rufen Sie an oder kommen Sie bei uns in Wendelsau vorbei.</p>
      </div>
    </div>
    <div class="panel p2">
      <h2 class="heading" style="right:26px;top:30px">So finden Sie uns</h2>
      <div class="body" style="left:30px;top:70px;width:270px;font-size:10.2px;line-height:16px">
        <p>Wir sind in Wendelsau im Haus von Falbrecht Flugbau untergebracht. Mit dem Auto können Sie auf das Gelände von Falbrecht Flugbau fahren und es auf den Parkplätzen neben dem Gebäude parken. Auf dieser Seite befindet sich ebenfalls der Eingang. Wir sind täglich ab 09:30 Uhr für Sie da.</p>
        <p>Im Foyer liegen unsere Flyer und Informationsbroschüren aus – hier finden Sie alle notwendigen Informationen vor.</p>
        <p>Besuchen Sie uns mit den öffentlichen Verkehrsmitteln: Fahren Sie mit der S-Bahn S3 bis zum Bahnhof Wendelsau und folgen anschließend dem Fußweg in Richtung des Flugplatzes Wendelsau in südlicher Richtung.</p>
      </div>
      <h2 class="heading" style="right:26px;top:377px">Kontakt</h2>
      <div class="subline" style="top:404px">Im Haus von Falbrecht Flugbau</div>
      <div class="contact" style="top:443px">Lindenhof-Weg 12<br>63411 Wendelsau<br>Tel.: 06104 - 555 120 40<br>e-mail: info@tl-luftdienst.de<br>www.tl-luftdienst.de</div>
      <div class="wordmark" style="left:20px;top:640px">Talwerk Luftdienst</div>
    </div>
    <div class="panel p3">
      <div class="photo-right" role="img" aria-label="Foto: Skyline einer Großstadt mit Kleinflugzeug im Flug"></div>
      <svg style="position:absolute;left:0;top:0" width="327" height="693" viewBox="0 0 327 693">
        <circle cx="197" cy="96" r="147" fill="var(--blue)" opacity=".92"/>
      </svg>
      <div class="claim" style="left:85px;top:58px">Noch nie war<br>fliegen so<br>sicher &amp; günstig<br>zugleich</div>
      <div class="wordmark" style="right:20px;top:664px">Talwerk Luftdienst</div>
    </div>
  </section>
</div>

<!-- ========== PRESENTATION: INSIDE ========== -->
<div class="mock" style="top:2341px">
  <section class="sheet inside">
    <svg class="art" viewBox="0 0 980 693">
      <circle cx="103" cy="78" r="120" fill="var(--blue)"/>
      <g role="img" aria-label="Foto: Stadt-Skyline im Abendlicht"><circle cx="115" cy="585" r="84" fill="#c29c78"/></g>
      <circle cx="490" cy="112" r="130" fill="var(--blue)"/>
      <g role="img" aria-label="Foto: Kleinflugzeug auf der Startbahn"><circle cx="490" cy="700" r="118" fill="#a8b1a5"/></g>
      <path d="M620,0 C570,150 600,330 720,385 C800,415 900,400 980,385 L980,0 Z" fill="var(--navy)"/>
      <g role="img" aria-label="Foto: Cockpit-Instrumente"><circle cx="874" cy="533" r="108" fill="#44474b"/></g>
    </svg>
    <div class="panel p1">
      <h2 class="heading on-blue" style="left:49px;top:58px;font-size:20px">Rundflüge</h2>
      <div class="intro" style="left:49px;top:84px;width:130px">Die Welt von oben sehen –<br>Wir machen es möglich</div>
      <div class="body" style="left:43px;top:208px;width:268px;font-size:10.3px;line-height:16px">
        <p>Die Frankfurter Skyline aus der Vogelperspektive betrachten? Das eigene Haus, Ihre Wohnung oder den Garten von oben sehen? Dann sind Sie bei der Talwerk Luftdienst in Wendelsau genau richtig.</p>
        <p style="margin-bottom:0">So könnte Ihr Rundflug aussehen:</p>
        <p><b>Beispiel 1:</b> Platzrunden-Rundflug mit 1 Person (max. 100 Kg) ab Wendelsau für 29€</p>
        <p><b>Beispiel 2:</b> 30 Minuten Rundflug für 1 Person (max. 100 Kg) ab Wendelsau für 109€ (ideal für einen Skyline Rundflug), aktuell für 99€.</p>
        <p><b>Beispiel 3:</b> 30 Minuten Rundflug mit bis zu 3 Personen (insg. max. 200 Kg) ab Wendelsau für 199€ regulär (ideal für einen Skyline Rundflug), aktuell für 179€.</p>
      </div>
    </div>
    <div class="panel p2">
      <h2 class="heading on-blue" style="left:0;width:326px;text-align:center;top:82px;font-size:19px">Pilotenausbildung</h2>
      <ul class="courses" style="left:60px;top:118px"><li>• PPL-A</li><li>• IFR</li><li>• ATPL-A</li><li>• AZF</li><li>• En-Route IFR</li></ul>
      <ul class="courses" style="left:150px;top:118px"><li>• MEP (auf der • FB42)</li><li>• CPL</li><li>• BZF I+II</li><li>• Nachtflugausbildung</li><li>• Competency IR</li></ul>
      <div class="body" style="left:43px;top:282px;width:240px;font-size:10.3px;line-height:16px">
        <p>In Zusammenarbeit mit unseren Kooperationspartnern können Sie bei der Talwerk Luftdienst ab sofort Pilot werden! Sie haben die Möglichkeit im Rahmen unserer Pilotenausbildung die Flugscheine PPL-A bis ATPL-A zu erreichen.</p>
        <p>Ihre praktische Flugausbildung werden Sie auf der modernen Flotte von Talwerk Luftdienst durchführen. Der Vorteil dabei: Sie werden von den klassischen Fluginstrumenten bis hin zum modernen „Glascockpit“ ein abgerundetes Angebot erhalten – und jederzeit selbst entscheiden dürfen, ob Sie klassische Instrumente oder moderne Anzeigegeräte bevorzugen.</p>
      </div>
    </div>
    <div class="panel p3">
      <h2 class="heading" style="left:7px;top:12px;font-size:24px">Charter &amp; Flotte</h2>
      <div class="chart-col" style="left:7px">
        <p>Unsere Preise verstehen sich inklusive 19 % Mehrwertsteuer und Treibstoffkosten. Landegebühren, Abstellgebühren sowie Handling-Fees der jeweiligen Airports usw. sind nicht im Preis enthalten.</p>
        <p>Abgerechnet wird nach Blockstunden in den jeweiligen Flugzeugen. Die Stundenzähler werden vor und nach jedem Flug von einem unserer Mitarbeiter gemeinsam mit Ihnen abgelesen</p>
      </div>
      <div class="chart-col" style="left:166px;width:145px">
        <p>und in das Übergabeprotokoll eingetragen. So haben Sie eine transparente Übersicht. Zu jeder Abrechnung erhalten Sie vor Ort eine Rechnung.</p>
        <p class="prices">• FB20-100 mit Navis 660 159€ pro Stunde Nassmiete</p>
        <p class="prices">• FB40 IFR/AP OE-KTA 249€ pro Stunde Nassmiete</p>
        <p class="prices">• FB42 TDI OE-KTC 519€ pro Stunde Nassmiete</p>
      </div>
    </div>
  </section>
</div>

</body>
</html>
```